Make a website for Velmora, a Luxury and Modern Concierge Platform based in the UAE

Concierge Platform that has various luxury and exotic actives available to clients, itinerary planning for a dubai / uae based holiday.
Want the website to appear luxury, modern and easy to understand, with a landing page that can captivate customers, majority will use Mobile but Desktop should look good too. Whatsapp Contact pop-out, and email sign up list. Social Link (Facebook, Instagram, Whatsapp, Whatsapp Broadcast, Twitter/X, etc).
Ability to make it Dark and Light themed.
Second page Page that has a list of activities on a drop down/ list, as follows:
Flights
Car Rental
Luxury Car Rental
Chauffer
Yachts/ Boats
Jet Ski / Watersports
Buggies/ ATV
Dining
Tickets/Events
Apartments/ Hotels
Personal Shopping.
Link to competitors, who's websites appear basic and could be 100% improved, for examples:
- https://www.quietharbourstays.example/
- https://www.tivra.example/
- https://www.gulf-latch.example/
- https://thelomarenhouse.example/dubai.html
- https://www.theplatinumhostdesk.example/concierge-service-dubai/
Open to logo designs, we own Velmora.com.
Colours:
Luxury Style, Black and Gold is often used, but maybe over-used?
A modern colour palette White, Light Blue, Light Grey, but we aren't experts at this, so this isn't by any means strict criteria, let the creative mind run free.
Thank you

```html
<!DOCTYPE html>
<html lang="en">
<head>
<meta charset="utf-8">
<title>Velmora — Experience Dubai Like Never Before</title>
<link rel="stylesheet" href="https://fonts.googleapis.com/css2?family=Gilda+Display&family=Poppins:wght@300;400;500&display=swap">
<style>
:root{
  --gold:#b49a62;
  --gold-dark:#9c8450;
  --ink:#151515;
  --text:#3d3d3d;
  --muted:#7a7a7a;
  --paper:#ffffff;
  --mist:#f7f6f3;
  --line:#e3e0da;
  --footer:#121212;
  --serif:'Gilda Display', Georgia, serif;
  --sans:'Poppins', Arial, sans-serif;
}
*{box-sizing:border-box;margin:0;padding:0}
html,body{width:1200px;height:5089px;overflow:hidden}
body{position:relative;background:var(--paper);font-family:var(--sans);color:var(--text)}
.abs{position:absolute}
.btn{position:absolute;display:flex;align-items:center;justify-content:center;background:var(--gold);color:#fff;font:500 12px var(--sans);letter-spacing:.06em;text-transform:uppercase}
.serif{font-family:var(--serif);font-weight:400;color:var(--ink)}

/* hero */
.hero{position:absolute;left:0;top:0;width:1200px;height:716px;background:
  radial-gradient(ellipse 60% 30% at 50% 92%,#f2a74a 0%,rgba(242,167,74,0) 70%),
  linear-gradient(180deg,#5b5fa8 0%,#8c74b8 18%,#c98aa6 32%,#6a7fb5 50%,#2d3f6b 70%,#3a2c3e 85%,#b8652c 100%)}
.topbar{position:absolute;left:76px;right:76px;top:0;height:75px;border-bottom:1px solid rgba(255,255,255,.35)}
.social-dot{position:absolute;top:31px;width:24px;height:24px;border-radius:50%;background:rgba(255,255,255,.22);border:1px solid rgba(255,255,255,.5)}
.logo{font-family:var(--serif);color:#fff;font-size:38px;position:absolute;left:0;right:0;top:16px;text-align:center}
.hero-title{position:absolute;left:0;right:0;top:235px;text-align:center;font-family:var(--serif);color:#fff;font-size:98px;line-height:1}
.hero-sub{position:absolute;left:500px;top:352px;font-family:var(--serif);color:#fff;font-size:34px}
.thumbs{position:absolute;left:0;top:619px;width:287px;height:144px;background:#fff}
.thumb{position:absolute;top:16px;width:130px;height:128px}

/* welcome */
.welcome-photo{left:565px;top:832px;width:546px;height:435px;background:linear-gradient(180deg,#cfd8de 0%,#9fb0bc 40%,#c4a37e 75%,#5f84b3 100%)}
.p{font-size:12.5px;line-height:21px;color:var(--text)}

/* services band */
.band{position:absolute;left:0;width:1200px;background:var(--mist)}
.arrow{position:absolute;top:1333px;width:38px;height:38px;display:flex;align-items:center;justify-content:center;color:#fff;font-size:14px}
.card{position:absolute;width:229px;overflow:hidden;box-shadow:0 18px 30px rgba(0,0,0,.14)}
.card .shade{position:absolute;inset:0;background:linear-gradient(180deg,rgba(0,0,0,0) 45%,rgba(0,0,0,.55) 100%)}
.card h3{position:absolute;left:20px;font:400 19px var(--serif);color:#fff}
.card span{position:absolute;left:20px;font-size:10.5px;color:#fff}

/* video */
.video{left:0;top:1773px;width:1200px;height:546px;background:linear-gradient(180deg,#e9d4cf 0%,#f1dfd6 45%,#c9b7ae 75%,#5e5a62 100%)}
.play{left:541px;top:1988px;width:116px;height:116px;border-radius:50%;background:#fff;box-shadow:0 0 0 10px rgba(255,255,255,.35);display:flex;align-items:center;justify-content:center}
.watch{left:0;right:0;top:2140px;text-align:center;font:400 104px var(--serif);color:rgba(255,255,255,.45)}

/* why */
.why-item{position:absolute;top:3473px;width:190px;height:190px;text-align:center}
.why-item svg{position:absolute;left:71px;top:26px}
.why-item h4{position:absolute;left:0;right:0;top:82px;font:400 16px/22px var(--serif);color:var(--ink)}
.why-item p{position:absolute;left:20px;right:20px;top:140px;font-size:11.5px;line-height:20px;color:var(--muted)}
.why-item.active{background:var(--gold);box-shadow:0 18px 30px rgba(0,0,0,.12)}
.why-item.active h4,.why-item.active p{color:#fff}

/* footer */
.footer{left:0;top:4494px;width:1200px;height:595px;background:var(--footer)}
.fcol{position:absolute;top:4685px}
.fcol h5{font:400 21px var(--serif);color:#fff;margin-bottom:18px}
.fcol li{list-style:none;font-size:11px;color:#d6d6d6;line-height:28px}
.fsocial{position:absolute;top:5040px;width:32px;height:32px;border-radius:50%;border:1.5px solid #fff}
.flinks{right:76px;top:5050px;font-size:10.5px;color:#d6d6d6}
</style>
</head>
<body>

<header class="hero" role="img" aria-label="Dubai skyline at dusk with the tallest tower lit against a violet sunset sky">
  <div class="topbar">
    <div class="social-dot" style="left:16px"></div>
    <div class="social-dot" style="left:56px"></div>
    <div class="social-dot" style="left:96px"></div>
    <div class="social-dot" style="left:136px"></div>
    <div class="social-dot" style="left:176px"></div>
    <div class="logo">Velmora</div>
    <div class="social-dot" style="right:40px;background:rgba(255,255,255,.85)"></div>
    <div class="social-dot" style="right:0"></div>
  </div>
  <h1 class="hero-title">Experience Dubai</h1>
  <div class="hero-sub">Like Never Before</div>
  <div class="btn" style="left:777px;top:356px;width:208px;height:41px;font-size:11.5px">Plan Your Experience</div>
</header>
<div class="thumbs">
  <div class="thumb" role="img" aria-label="Dubai marina towers" style="left:0;background:linear-gradient(180deg,#8fb1d6,#c9a274)"></div>
  <div class="thumb" role="img" aria-label="Dubai waterfront skyline" style="left:143px;background:linear-gradient(180deg,#4c86c9,#c2c6cc)"></div>
</div>

<!-- welcome -->
<h2 class="abs serif" style="left:89px;top:898px;font-size:36px">Welcome to Velmora</h2>
<p class="abs p" style="left:90px;top:958px;width:430px">Experience Dubai like never before. Whether you're looking for VIP access, luxury travel, or exclusive entertainment, Velmora offers tailored concierge services that transform your trip into a seamless, unforgettable journey. From private yachts to exotic supercars, we curate every detail for you.</p>
<div class="btn" style="left:91px;top:1085px;width:168px;height:46px">Discover More</div>
<div class="abs welcome-photo" role="img" aria-label="Woman walking among palm trees toward Dubai towers"></div>

<!-- services -->
<div class="band" style="top:1206px;height:567px"></div>
<h2 class="abs serif" style="left:89px;top:1328px;font-size:36px">Your Luxury, Your Way</h2>
<div class="arrow" style="left:1024px;background:var(--ink)">&#8249;</div>
<div class="arrow" style="left:1073px;background:var(--gold)">&#8250;</div>

<div class="card" style="left:89px;top:1449px;height:202px;background:linear-gradient(180deg,#7fb0d6,#bcd2e2)" role="img" aria-label="Private jet flying between towers">
  <div class="shade"></div><h3 style="top:130px">Flights</h3><span style="top:161px">Private jets &amp; first-class travel</span></div>
<div class="card" style="left:354px;top:1404px;height:290px;background:linear-gradient(180deg,#cdb78f,#3a3a3c)" role="img" aria-label="Black luxury saloon car">
  <div class="shade"></div><h3 style="top:218px">Car Rental</h3><span style="top:249px">From SUVs to economy cars</span></div>
<div class="card" style="left:619px;top:1449px;height:202px;background:linear-gradient(180deg,#9aa8b8,#2e3138)" role="img" aria-label="Luxury SUV parked at night">
  <div class="shade"></div><h3 style="top:130px">Luxury Car Rental</h3><span style="top:161px">Supercars &amp; elite rides</span></div>
<div class="card" style="left:882px;top:1404px;height:290px;background:linear-gradient(180deg,#c7c4bb,#7f8b90)" role="img" aria-label="White yachts moored in a marina">
  <div class="shade"></div><h3 style="top:218px">Yachts &amp; Boats</h3><span style="top:249px">Cruise in style</span></div>
<div class="card" style="left:1147px;top:1449px;height:202px;background:linear-gradient(180deg,#5b9fc9,#2a6f9a)" role="img" aria-label="Jet ski on open water">
  <div class="shade"></div><h3 style="top:130px">Jet Ski</h3><span style="top:161px">Thrill rides</span></div>

<!-- video -->
<div class="abs video" role="img" aria-label="Flag flying beside the tallest tower in Dubai"></div>
<div class="abs play"><svg width="22" height="24" viewBox="0 0 22 24"><path d="M3 2l17 10L3 22z" fill="#111"/></svg></div>
<div class="abs watch">watch our video</div>

<!-- weekend offer -->
<div class="abs" role="img" aria-label="Hand holding a glass sphere reflecting the Dubai skyline" style="left:132px;top:2404px;width:493px;height:415px;background:linear-gradient(180deg,#d7d9dc,#a69c90 60%,#8b6f58)"></div>
<h2 class="abs serif" style="left:684px;top:2466px;font-size:36px;line-height:49px">High-end Weekend<br>Double Up On Luxury</h2>
<p class="abs p" style="left:684px;top:2573px;font-size:12px">Book any two services over the weekend &amp; unlock:</p>
<div class="abs" style="left:684px;top:2612px;font:400 48px var(--serif);color:var(--gold)">25% OFF</div>
<div class="abs" style="left:684px;top:2670px;font-size:11.5px;color:var(--gold)">Your Second Booking</div>
<div class="btn" style="left:684px;top:2710px;width:253px;height:44px">Plan Your Weekend Escape</div>

<!-- flash deals -->
<div class="band" style="top:3272px;height:468px"></div>
<h2 class="abs serif" style="left:132px;top:2940px;font-size:36px;line-height:49px">Flash Luxury Deals<br>Limited Time Offers</h2>
<p class="abs p" style="left:132px;top:3050px;width:430px;font-size:12px">Exclusivity comes with perfect timing. Secure these members only perks before they disappear:</p>
<div class="abs" style="left:132px;top:3105px;font:400 13px/24px var(--serif);color:var(--ink)">
  <div><span style="color:var(--gold)">&#9670;</span> 50% OFF Sunset Yacht Charters (Weekdays Only)</div>
  <div><span style="color:var(--gold)">&#9670;</span> Complimentary Personal Butler for Suite Bookings Over 3 Nights</div>
</div>
<div class="btn" style="left:132px;top:3169px;width:202px;height:45px">Unlock Flash Deals</div>
<div class="abs" role="img" aria-label="Traveller with hat and backpack overlooking Dubai Marina" style="left:625px;top:2894px;width:575px;height:451px;background:linear-gradient(180deg,#c9dbe9,#8fb0c8 50%,#c9a883 80%,#4f6a82)"></div>

<!-- why -->
<h2 class="abs serif" style="left:0;right:0;top:3400px;text-align:center;font-size:36px">Why Velmora?</h2>
<div class="why-item" style="left:182px">
  <svg width="48" height="48" viewBox="0 0 48 48" fill="none" stroke="#222" stroke-width="1.6"><path d="M12 16h24l6 8-18 18L6 24z M6 24h36 M18 16l6 26 6-26"/></svg>
  <h4>Luxury at<br>Your Fingertips</h4><p>Premium services tailored for you</p></div>
<div class="why-item" style="left:391px">
  <svg width="48" height="48" viewBox="0 0 48 48" fill="none" stroke="#222" stroke-width="1.6"><circle cx="24" cy="24" r="18"/><text x="24" y="29" text-anchor="middle" font-family="Poppins,sans-serif" font-size="12" fill="#222" stroke="none">24/7</text></svg>
  <h4>24/7 Concierge<br>Support</h4><p>Your personal assistant in Dubai</p></div>
<div class="why-item active" style="left:619px">
  <svg width="48" height="48" viewBox="0 0 48 48" fill="none" stroke="#fff" stroke-width="1.6"><circle cx="24" cy="20" r="14"/><circle cx="24" cy="20" r="8"/><path d="M16 32l-4 12 7-3 5 5 M32 32l4 12-7-3"/></svg>
  <h4>Exclusive<br>Access</h4><p>Get behind the velvet rope</p></div>
<div class="why-item" style="left:832px">
  <svg width="48" height="48" viewBox="0 0 48 48" fill="none" stroke="#222" stroke-width="1.6"><rect x="6" y="6" width="36" height="14" rx="3"/><text x="24" y="16" text-anchor="middle" font-family="Poppins,sans-serif" font-size="8" fill="#222" stroke="none">BOOK</text><path d="M22 24v16l-5-4 M22 24h4v8h6v10H20"/></svg>
  <h4>Seamless<br>Booking</h4><p>Instant, hassle-free reservations</p></div>
<div class="abs" style="left:122px;top:3734px;width:956px;height:1px;background:var(--line)"></div>

<!-- featured -->
<h2 class="abs serif" style="left:0;right:0;top:3780px;text-align:center;font-size:36px">Featured Experiences</h2>
<div class="card" style="left:89px;top:3902px;height:204px;background:linear-gradient(180deg,#e2c8b0,#8a6b58)" role="img" aria-label="Helicopter above desert mountains">
  <div class="shade"></div><h3 style="top:132px">Helicopter Tour</h3><span style="top:163px">Private jets &amp; first-class travel</span></div>
<div class="card" style="left:354px;top:3859px;height:291px;background:linear-gradient(180deg,#cdb78f,#3a3a3c)" role="img" aria-label="Black luxury saloon car">
  <div class="shade"></div><h3 style="top:219px">Car Rental</h3><span style="top:250px">From SUVs to economy cars</span></div>
<div class="card" style="left:619px;top:3902px;height:204px;background:linear-gradient(180deg,#8aa0b8,#d8d6d0)" role="img" aria-label="White luxury car outside a hotel">
  <div class="shade"></div><h3 style="top:132px">Luxury Car Rental</h3><span style="top:163px">Supercars &amp; elite rides</span></div>
<div class="card" style="left:882px;top:3859px;height:291px;background:linear-gradient(180deg,#d9a785,#6b7e94 60%,#3e5266)" role="img" aria-label="Yachts cruising past the marina at sunset">
  <div class="shade"></div><h3 style="top:219px">Yachts &amp; Boats</h3><span style="top:250px">Cruise in style</span></div>
<div class="btn" style="left:538px;top:4179px;width:124px;height:46px">See More</div>

<!-- testimonial -->
<div class="abs" style="left:236px;top:4230px;font:400 170px var(--serif);color:#eeece8;line-height:1">&ldquo;</div>
<h2 class="abs serif" style="left:0;right:0;top:4296px;text-align:center;font-size:36px">What Our Clients Say</h2>
<p class="abs p" style="left:0;right:0;top:4358px;text-align:center;font-size:12.5px;line-height:23px">From the moment we landed in Dubai, everything was taken care of. The luxury yacht,<br>VIP dining, and private chauffeur made this trip unforgettable.</p>
<div class="abs" style="left:0;right:0;top:4418px;text-align:center;font:400 15px var(--serif);color:var(--gold)">Harriet, London</div>

<!-- footer -->
<footer class="abs footer"></footer>
<div class="abs" style="left:0;right:0;top:4520px;text-align:center;font:400 84px var(--serif);color:#fff;line-height:1">Velmora</div>
<div class="abs" style="left:89px;top:4640px;width:1022px;height:1px;background:#3a3a3a"></div>
<div class="fcol" style="left:125px"><h5>Browse homes in</h5><ul><li>All Locations</li><li>Al Raha Beach</li><li>Saadiyat Island</li><li>Al Reem Island</li><li>Yas Island</li><li>Khalifa City</li><li>Al Mushrif</li><li>Al Reef</li></ul></div>
<div class="fcol" style="left:382px"><h5>Neighbourhood guides</h5><ul><li>All Locations</li><li>Al Barari</li><li>District One</li><li>Downtown Dubai</li><li>Dubai Hills</li><li>Emirates Hills</li><li>Jumeirah Bay</li><li>Island</li><li>Jumeirah Golf</li></ul></div>
<div class="fcol" style="left:694px"><h5>Company</h5><ul style="line-height:22px"><li style="line-height:22px">Contact Us</li><li style="line-height:22px">About Us</li><li style="line-height:22px">Meet Our Concierge</li><li style="line-height:22px">Careers</li><li style="line-height:22px">Travel Insurance</li><li style="line-height:22px">Holiday Extras</li><li style="line-height:22px">FAQs</li></ul></div>
<div class="fcol" style="left:907px"><h5>Legal</h5><ul><li style="line-height:22px">Booking Terms &amp; Conditions</li><li style="line-height:22px">Visa Information</li><li style="line-height:22px">Your Key Rights</li><li style="line-height:22px">Modern Slavery Statement</li><li style="line-height:22px">Privacy Policy</li><li style="line-height:22px">Cookie Policy</li><li style="line-height:22px">Sitemap</li></ul></div>
<div class="abs" style="left:89px;top:5050px;font-size:10.5px;color:#d6d6d6">&copy; Copyright 2025 Velmora Real Estate, All Rights Reserved</div>
<div class="fsocial" style="left:523px" aria-label="Social link"></div>
<div class="fsocial" style="left:563px" aria-label="Social link"></div>
<div class="fsocial" style="left:603px" aria-label="Social link"></div>
<div class="fsocial" style="left:643px" aria-label="Social link"></div>
<div class="abs flinks">Terms of Use &nbsp;|&nbsp; Privacy Policy &nbsp;|&nbsp; Archives &nbsp;|&nbsp; Project Archives</div>
<div class="abs" style="left:1131px;top:5000px;width:48px;height:48px;border-radius:50%;background:var(--gold);display:flex;align-items:center;justify-content:center">
  <svg width="14" height="10" viewBox="0 0 14 10"><path d="M2 8l5-5 5 5" stroke="#fff" stroke-width="2" fill="none"/></svg>
</div>

</body>
</html>
```